Designing a website for Brightmoor Pest Services PTY LTD

Pest control company looking for someone to build an informative website containing services we offer and an online inquiry form.
Commercial premises - Specialising in - Rodent control, stored product pest control, flying insect control, ant, spider and insect control, Termite inspections and treatments. Termite management systems on a commercial scale.
Facilities we service
Commercial - shopping centres, transport facilities, restaurants, pubs, clubs, bars food manufacturing facilities.
Residential - Houses specialising in - Rodent, Ant, Spider, Cockroach and Termite control. Termite inspections, Pre - purchase inspections, Termite treatments, Termite management systems.
Target Market(s)
Mainly commercial and industrial clients and Residential clients.
Industry/Entity Type
Pest Control
Number of Pages Required
1 page
Look and feel

```html
<!DOCTYPE html>
<html lang="en">
<head>
<meta charset="utf-8">
<title>Brightmoor Pest Services</title>
<link href="https://fonts.googleapis.com/css2?family=Kanit:wght@400;500;600&family=Poppins:wght@400;500;600&display=swap" rel="stylesheet">
<style>
:root{
  --green:#3d9313;
  --green-dark:#2c6a0d;
  --green-soft:#e7f1df;
  --ink:#1b1b1b;
  --text:#555;
  --white:#fff;
  --black:#050505;
  --line:#cfcfcf;
}
*{box-sizing:border-box;margin:0;padding:0}
html,body{width:1200px;height:4862px;overflow:hidden}
body{position:relative;background:var(--white);font-family:'Poppins',sans-serif;color:var(--ink)}
.abs{position:absolute}
.center-text{text-align:center;left:0;width:1200px}
.btn{position:absolute;display:flex;align-items:center;justify-content:center;background:var(--green);color:var(--white);font-family:'Poppins',sans-serif;font-weight:500;font-size:14px;border-radius:22px}
.heading{font-family:'Kanit',sans-serif;font-weight:500;font-size:34px;color:var(--ink);letter-spacing:.3px}
.heading .accent{color:var(--green)}
.lede{font-size:12px;line-height:20px;color:var(--text)}
.brand-name{font-family:'Kanit',sans-serif;font-weight:600;color:var(--ink);white-space:nowrap}

/* top bar & nav */
.top-bar{top:0;left:0;width:1200px;height:32px;background:var(--green)}
.social{top:9px;width:13px;height:13px;border-radius:50%;background:var(--white)}
.call{top:7px;right:60px;color:var(--white);font-size:13px;display:flex;align-items:center;gap:8px}
.nav{top:32px;left:0;width:1200px;height:72px;background:var(--white)}
.nav-link{top:60px;font-size:12px;color:#333}
.nav-link.active{color:var(--green)}
.nav-active-mark{top:49px;left:381px;width:54px;height:22px;border:2px solid var(--green);border-radius:50%;border-right-color:transparent;border-bottom-color:transparent}
.book-top{top:48px;left:990px;width:150px;height:40px;background:var(--black);font-size:13px}

/* hero */
.hero{top:104px;left:0;width:1200px;height:609px;background:linear-gradient(180deg,#eef0f2 0%,#d4d8dc 30%,#8d8e8a 52%,#6f9240 72%,#4b7c1f 100%)}
.hero-kicker{top:276px;right:92px;font-size:18px;color:#333}
.hero-title{right:92px;font-family:'Kanit',sans-serif;font-weight:500;font-size:58px;line-height:58px}
.hero-sub{top:426px;right:92px;font-size:17px;color:#222}
.dot{top:675px;width:11px;height:11px;border-radius:50%;background:var(--white)}
.dot.current{background:var(--green);border:2px solid var(--white)}

/* services diagram */
.svc-label{font-size:11.5px;line-height:16px;color:#333}

/* about */
.about{top:1445px;left:0;width:1200px;height:523px;background:var(--green)}
.about-kicker{top:1543px;left:134px;color:var(--white);font-size:15px}
.about-title{top:1568px;left:134px;font-family:'Kanit',sans-serif;font-weight:500;font-size:34px;color:var(--black);white-space:nowrap}
.about-title .light{color:var(--white)}
.about-copy{left:134px;width:380px;color:var(--white);font-size:11px;line-height:20px}
.outline-btn{top:1790px;left:134px;width:136px;height:40px;border:2px solid var(--white);border-radius:22px;color:var(--white);font-size:13px;font-weight:500;display:flex;align-items:center;justify-content:center}
.tile{border-radius:38px}
.tile.dark{background:var(--green-dark)}

/* facility sections */
.band{left:0;width:1200px}
.card{left:109px;width:982px;background:var(--white);border-radius:76px 76px 0 0}
.fac{text-align:center;font-size:12.5px;line-height:19px;color:#222;width:200px}
.fac-icon{display:block;margin:0 auto 6px}

/* inquiry */
.inquiry{top:3840px;left:0;width:1200px;height:525px;background:linear-gradient(180deg,#ffffff 0%,#eef5e8 35%,#d6e8c8 100%)}
.field{height:40px;border:1.5px solid #cfd6c9;border-radius:20px;background:var(--white);font-size:10px;color:#777;padding:0 16px;display:flex;align-items:center;justify-content:space-between}
.field.first{border-color:var(--green)}

/* call band & footer */
.call-band{top:4365px;left:0;width:1200px;height:96px;background:var(--green);display:flex;align-items:center;justify-content:center;gap:26px}
.call-band-text{color:var(--white);font-family:'Kanit',sans-serif;font-size:23px;white-space:nowrap}
.call-pill{height:48px;border-radius:24px;background:var(--green-dark);display:flex;align-items:center;gap:14px;padding:0 26px 0 12px;color:var(--white);font-family:'Kanit',sans-serif;font-size:23px;white-space:nowrap}
.footer{top:4461px;left:0;width:1200px;height:401px;background:var(--black)}
.foot-head{top:4494px;color:var(--white);font-size:14px;font-weight:500}
.foot-list{list-style:none;color:#d9d9d9;font-size:11px;line-height:22.6px}
.foot-list li::before{content:"";display:inline-block;width:4px;height:4px;border-radius:50%;background:var(--green);margin-right:14px;vertical-align:middle}
.foot-contact{color:#d9d9d9;font-size:11px;line-height:17px}
</style>
</head>
<body>

<!-- top bar -->
<div class="abs top-bar"></div>
<span class="abs social" style="left:69px"></span>
<span class="abs social" style="left:99px;border-radius:3px"></span>
<svg class="abs" style="top:9px;left:127px" width="15" height="12" viewBox="0 0 15 12"><rect x="0.5" y="0.5" width="14" height="11" rx="1.5" fill="#fff"/><path d="M1 1.5l6.5 5 6.5-5" stroke="#3d9313" stroke-width="1.4" fill="none"/></svg>
<div class="abs call">
  <svg width="10" height="17" viewBox="0 0 10 17"><rect x="1" y="1" width="8" height="15" rx="1.5" fill="none" stroke="#fff" stroke-width="1.6"/><circle cx="5" cy="13" r="1" fill="#fff"/></svg>
  Call Us : +1 555 014 2288
</div>

<!-- nav -->
<nav class="abs nav"></nav>
<span class="abs nav-active-mark"></span>
<span class="abs nav-link active" style="left:390px">Home</span>
<span class="abs nav-link" style="left:453px">Services</span>
<span class="abs brand-name" style="top:50px;left:512px;width:176px;text-align:center;font-size:17px;line-height:20px">Brightmoor<br>Pest Services</span>
<span class="abs nav-link" style="left:694px">About Us</span>
<span class="abs nav-link" style="left:774px">Contact Us</span>
<div class="btn book-top">BOOK ONLINE</div>

<!-- hero -->
<section class="abs hero" role="img" aria-label="Technician in protective suit and respirator with a spray wand in front of a two-storey house on a green lawn, with round insect insets"></section>
<p class="abs hero-kicker">Perfect Pest Control System !</p>
<h1 class="abs hero-title" style="top:305px;color:var(--green)">SAFE WAYS</h1>
<h1 class="abs hero-title" style="top:362px;color:var(--black)">TO CONTROL</h1>
<p class="abs hero-sub">Pest Around Your Home And Workplace</p>
<div class="btn" style="top:464px;left:960px;width:148px;height:38px;font-size:14px">BOOK ONLINE</div>
<span class="abs dot" style="left:597px"></span>
<span class="abs dot current" style="left:615px"></span>
<span class="abs dot" style="left:633px"></span>
<span class="abs dot" style="left:651px"></span>

<!-- services we offer -->
<h2 class="abs heading center-text" style="top:778px">SERVICES <span class="accent">WE OFFER</span></h2>
<p class="abs lede center-text" style="top:828px">Lorem Ipsum has been the industry's standard dummy text ever since the when an<br>unknown printer took a galley of type and scrambled.</p>

<svg class="abs" style="top:900px;left:0" width="1200" height="420" viewBox="0 900 1200 420">
  <g fill="none" stroke="#3d9313" stroke-width="1.3">
    <path d="M441 932 A189 189 0 1 0 767 932"/>
    <line x1="353" y1="959" x2="428" y2="959"/>
    <line x1="274" y1="1051" x2="416" y2="1051"/>
    <line x1="353" y1="1140" x2="452" y2="1140"/>
    <line x1="780" y1="959" x2="843" y2="959"/>
    <line x1="792" y1="1051" x2="925" y2="1051"/>
    <line x1="756" y1="1140" x2="843" y2="1140"/>
    <line x1="604" y1="1217" x2="604" y2="1272"/>
  </g>
  <g fill="#3d9313">
    <circle cx="428" cy="959" r="4"/><circle cx="416" cy="1051" r="4"/><circle cx="452" cy="1140" r="4"/>
    <circle cx="780" cy="959" r="4"/><circle cx="792" cy="1051" r="4"/><circle cx="756" cy="1140" r="4"/>
    <circle cx="604" cy="1217" r="4"/>
  </g>
  <circle cx="319" cy="959" r="34" fill="#3d9313"/>
  <g fill="#fff" stroke="#3d9313" stroke-width="2">
    <circle cx="240" cy="1051" r="34"/><circle cx="319" cy="1140" r="34"/>
    <circle cx="877" cy="959" r="34"/><circle cx="959" cy="1051" r="34"/><circle cx="877" cy="1140" r="34"/>
    <circle cx="604" cy="1306" r="34"/>
  </g>
  <g fill="none" stroke-width="2">
    <circle cx="319" cy="959" r="12" stroke="#fff"/>
    <circle cx="240" cy="1051" r="12" stroke="#1b1b1b"/><circle cx="319" cy="1140" r="12" stroke="#1b1b1b"/>
    <circle cx="877" cy="959" r="12" stroke="#1b1b1b"/><rect x="947" y="1039" width="24" height="24" rx="3" stroke="#1b1b1b"/>
    <circle cx="877" cy="1140" r="12" stroke="#1b1b1b"/><circle cx="604" cy="1306" r="12" stroke="#1b1b1b"/>
  </g>
</svg>
<span class="abs brand-name" style="top:1010px;left:454px;width:300px;text-align:center;font-size:38px;line-height:42px">Brightmoor<br>Pest Services</span>

<p class="abs svc-label" style="top:938px;left:150px;width:118px;text-align:right">Flying Insect<br>Control</p>
<p class="abs svc-label" style="top:1035px;left:60px;width:127px;text-align:right">Spider And Insect<br>Control</p>
<p class="abs svc-label" style="top:1129px;left:60px;width:211px;text-align:right">Termite management Systems<br>on a Commercial Scale.</p>
<p class="abs svc-label" style="top:943px;left:930px">Termite Inspections<br>And Treatments</p>
<p class="abs svc-label" style="top:1033px;left:1010px">Stored Product<br>Pest Control</p>
<p class="abs svc-label" style="top:1122px;left:931px">Rodent<br>Control</p>
<p class="abs svc-label" style="top:1352px;left:570px;width:68px;text-align:center">Ant</p>

<!-- about -->
<section class="abs about"></section>
<p class="abs about-kicker">About Us</p>
<h2 class="abs about-title">BRIGHTMOOR <span class="light">PEST SERVICES</span></h2>
<p class="abs about-copy" style="top:1622px">Lorem Ipsum has been the industry's standard dummy text ever since the 1500s, when an unknown printer took a galley of type and scrambled it to make a type specimen book.</p>
<p class="abs about-copy" style="top:1692px">It has survived not only five centuries, but also the leap into electronic typesetting, remaining essentially unchanged. It was popularised in the 1960s with the release of Letraset sheets containing Lorem Ipsum passages, more recently</p>
<div class="abs outline-btn">LEARN MORE</div>
<div class="abs tile dark" style="top:1445px;left:713px;width:123px;height:65px;border-radius:0 0 30px 30px"></div>
<div class="abs tile" style="top:1528px;left:625px;width:211px;height:235px;background:linear-gradient(135deg,#8a6a4c,#c9b69c 60%,#e9e4dc)" role="img" aria-label="Technician spraying along a kitchen floor skirting"></div>
<div class="abs tile" style="top:1445px;left:853px;width:213px;height:180px;border-radius:0 0 38px 38px;background:linear-gradient(135deg,#dfe5e8,#9eaab0 55%,#3f6f2a)" role="img" aria-label="Technician in protective suit spraying warehouse shelving"></div>
<div class="abs tile" style="top:1643px;left:853px;width:213px;height:235px;background:linear-gradient(135deg,#f2f2f0,#d8d6d0 55%,#8c6a44)" role="img" aria-label="Technician treating kitchen cabinets while a resident watches"></div>
<div class="abs tile dark" style="top:1778px;left:662px;width:46px;height:47px;border-radius:12px"></div>
<div class="abs tile dark" style="top:1778px;left:721px;width:115px;height:109px;border-radius:26px"></div>

<!-- residential -->
<div class="abs band" style="top:1968px;height:489px;background:linear-gradient(90deg,#e8e7e4 0%,#f3f3f1 45%,#c9b79c 75%,#7a5a3b 100%)" role="img" aria-label="Technician treating kitchen cabinets while a resident watches"></div>
<div class="abs card" style="top:2317px;height:600px"></div>
<h2 class="abs heading center-text" style="top:2388px">RESIDENTIAL <span class="accent">FACILITIES</span></h2>
<p class="abs lede center-text" style="top:2443px">Lorem Ipsum has been the industry's standard dummy text ever since the when an<br>unknown printer took a galley of type and scrambled.</p>

<div class="abs fac" style="top:2516px;left:181px"><svg class="fac-icon" width="54" height="54" viewBox="0 0 54 54"><ellipse cx="27" cy="30" rx="20" ry="12" fill="none" stroke="#1b1b1b" stroke-width="2"/><circle cx="14" cy="20" r="5" fill="none" stroke="#3d9313" stroke-width="2"/></svg>Houses specialising<br>in - Rodent</div>
<div class="abs fac" style="top:2516px;left:396px"><svg class="fac-icon" width="54" height="54" viewBox="0 0 54 54"><circle cx="27" cy="17" r="7" fill="none" stroke="#3d9313" stroke-width="2"/><ellipse cx="27" cy="35" rx="8" ry="11" fill="none" stroke="#1b1b1b" stroke-width="2"/></svg>Ant</div>
<div class="abs fac" style="top:2516px;left:615px"><svg class="fac-icon" width="54" height="54" viewBox="0 0 54 54"><circle cx="27" cy="27" r="10" fill="none" stroke="#3d9313" stroke-width="2"/><circle cx="27" cy="27" r="20" fill="none" stroke="#1b1b1b" stroke-width="2" stroke-dasharray="6 5"/></svg>Spider</div>
<div class="abs fac" style="top:2516px;left:832px"><svg class="fac-icon" width="54" height="54" viewBox="0 0 54 54"><ellipse cx="27" cy="30" rx="9" ry="15" fill="none" stroke="#1b1b1b" stroke-width="2"/><circle cx="27" cy="12" r="5" fill="none" stroke="#3d9313" stroke-width="2"/></svg>Cockroach and<br>Termite Control</div>
<div class="abs fac" style="top:2651px;left:181px"><svg class="fac-icon" width="54" height="54" viewBox="0 0 54 54"><ellipse cx="27" cy="31" rx="8" ry="15" fill="none" stroke="#1b1b1b" stroke-width="2"/><circle cx="27" cy="12" r="5" fill="none" stroke="#3d9313" stroke-width="2"/></svg>Termite<br>Inspections</div>
<div class="abs fac" style="top:2651px;left:396px"><svg class="fac-icon" width="54" height="54" viewBox="0 0 54 54"><path d="M8 26L24 12l16 14v20H8z" fill="none" stroke="#1b1b1b" stroke-width="2"/><circle cx="38" cy="34" r="7" fill="none" stroke="#3d9313" stroke-width="2"/><line x1="43" y1="39" x2="49" y2="45" stroke="#3d9313" stroke-width="2"/></svg>Pre - Purchase<br>Inspections</div>
<div class="abs fac" style="top:2651px;left:615px"><svg class="fac-icon" width="54" height="54" viewBox="0 0 54 54"><circle cx="27" cy="12" r="6" fill="none" stroke="#1b1b1b" stroke-width="2"/><path d="M16 48V26q11-8 22 0v22" fill="none" stroke="#1b1b1b" stroke-width="2"/><rect x="22" y="30" width="10" height="14" fill="none" stroke="#3d9313" stroke-width="2"/></svg>Termite management<br>systems.</div>
<div class="abs fac" style="top:2651px;left:832px"><svg class="fac-icon" width="54" height="54" viewBox="0 0 54 54"><ellipse cx="27" cy="31" rx="8" ry="16" fill="#e7f1df" stroke="#3d9313" stroke-width="2"/><circle cx="27" cy="11" r="5" fill="none" stroke="#1b1b1b" stroke-width="2"/></svg>Termite<br>Treatments</div>

<div class="btn" style="top:2813px;left:525px;width:150px;height:42px">BOOK ONLINE</div>

<!-- commercial -->
<div class="abs band" style="top:2930px;height:489px;background:linear-gradient(90deg,#55626a 0%,#8e9aa1 35%,#c9ccc9 55%,#9aa3a8 80%,#5e6a70 100%)" role="img" aria-label="Technician in protective suit and respirator treating a warehouse with a backpack sprayer"></div>
<div class="abs card" style="top:3278px;height:562px;border-radius:76px;box-shadow:0 14px 22px rgba(0,0,0,.07)"></div>
<h2 class="abs heading center-text" style="top:3344px">COMMERCIAL <span class="accent">FACILITIES</span></h2>
<p class="abs lede center-text" style="top:3396px">Lorem Ipsum has been the industry's standard dummy text ever since the when an<br>unknown printer took a galley of type and scrambled.</p>

<div class="abs fac" style="top:3465px;left:280px"><svg class="fac-icon" width="54" height="54" viewBox="0 0 54 54"><rect x="10" y="8" width="34" height="40" fill="none" stroke="#3d9313" stroke-width="2"/><path d="M16 16h22M16 24h22M16 32h22" stroke="#1b1b1b" stroke-width="2"/><rect x="23" y="38" width="8" height="10" fill="none" stroke="#1b1b1b" stroke-width="2"/></svg>Shopping Centres</div>
<div class="abs fac" style="top:3465px;left:500px"><svg class="fac-icon" width="54" height="54" viewBox="0 0 54 54"><rect x="8" y="8" width="38" height="12" fill="none" stroke="#1b1b1b" stroke-width="2"/><rect x="10" y="20" width="34" height="28" fill="none" stroke="#3d9313" stroke-width="2"/><rect x="18" y="28" width="18" height="12" fill="none" stroke="#1b1b1b" stroke-width="2"/></svg>Pubs</div>
<div class="abs fac" style="top:3465px;left:713px"><svg class="fac-icon" width="54" height="54" viewBox="0 0 54 54"><path d="M6 20L27 8l21 12" fill="none" stroke="#1b1b1b" stroke-width="2"/><rect x="10" y="20" width="34" height="28" fill="none" stroke="#3d9313" stroke-width="2"/><rect x="22" y="32" width="10" height="16" fill="none" stroke="#1b1b1b" stroke-width="2"/></svg>Clubs</div>
<div class="abs fac" style="top:3595px;left:280px"><svg class="fac-icon" width="54" height="54" viewBox="0 0 54 54"><path d="M8 48V24l12-8v8l12-8v8l12-8v32z" fill="none" stroke="#1b1b1b" stroke-width="2"/><rect x="26" y="30" width="12" height="12" fill="none" stroke="#3d9313" stroke-width="2"/></svg>Bars Food<br>Manufacturing Facilities</div>
<div class="abs fac" style="top:3595px;left:500px"><svg class="fac-icon" width="54" height="54" viewBox="0 0 54 54"><rect x="8" y="8" width="38" height="40" fill="none" stroke="#1b1b1b" stroke-width="2"/><rect x="14" y="20" width="26" height="20" fill="none" stroke="#3d9313" stroke-width="2"/><circle cx="19" cy="44" r="2" fill="#3d9313"/><circle cx="35" cy="44" r="2" fill="#3d9313"/></svg>Transport Facilities</div>
<div class="abs fac" style="top:3595px;left:713px"><svg class="fac-icon" width="54" height="54" viewBox="0 0 54 54"><path d="M8 12h38v8H8z" fill="none" stroke="#3d9313" stroke-width="2"/><rect x="10" y="20" width="34" height="28" fill="none" stroke="#1b1b1b" stroke-width="2"/><path d="M16 28h8v8h-8zM30 28h8v8h-8z" fill="none" stroke="#1b1b1b" stroke-width="2"/></svg>Restaurants</div>

<div class="btn" style="top:3743px;left:525px;width:150px;height:42px">BOOK ONLINE</div>

<!-- inquiry -->
<section class="abs inquiry" role="img" aria-label="Faded green-tinted photo of a pest control technician at work"></section>
<h2 class="abs heading center-text" style="top:3930px;font-size:32px;left:-10px">GET ONLINE INQUIRY</h2>
<p class="abs center-text" style="top:3980px;left:-10px;font-size:13px;color:var(--green)">Need Any Help or Support Contact Us For Better Help &amp; Services</p>
<div class="abs field first" style="top:4033px;left:323px;width:273px">Name *</div>
<div class="abs field" style="top:4033px;left:604px;width:273px">Services* <svg width="8" height="5" viewBox="0 0 8 5"><path d="M0 0h8L4 5z" fill="#333"/></svg></div>
<div class="abs field" style="top:4088px;left:323px;width:273px">Phone *</div>
<div class="abs field" style="top:4088px;left:604px;width:273px">Schedule date * <svg width="8" height="5" viewBox="0 0 8 5"><path d="M0 0h8L4 5z" fill="#333"/></svg></div>
<div class="abs field" style="top:4144px;left:323px;width:554px;height:89px;align-items:flex-start;padding-top:14px;border-radius:22px">Message *</div>
<div class="btn" style="top:4250px;left:541px;width:117px;height:38px">SUBMIT</div>

<!-- call band -->
<section class="abs call-band">
  <p class="call-band-text">365 Days Defend Your Pest Call Us :</p>
  <div class="call-pill">
    <svg width="32" height="32" viewBox="0 0 32 32"><circle cx="16" cy="16" r="14.5" fill="none" stroke="#fff" stroke-width="1.5"/><path d="M11 9l3 4-2 2q2 4 5 5l2-2 4 3-2 3q-9-1-12-12z" fill="none" stroke="#fff" stroke-width="1.4"/></svg>
    +1 555 014 2288
  </div>
</section>

<!-- footer -->
<footer class="abs footer"></footer>
<p class="abs foot-head" style="left:98px">SITEMAP</p>
<p class="abs foot-head" style="left:449px">SERVICES</p>
<p class="abs foot-head" style="left:802px">CONTACT US</p>
<ul class="abs foot-list" style="top:4537px;left:98px"><li>Home</li><li>Services</li><li>About Us</li><li>Contact Us</li></ul>
<ul class="abs foot-list" style="top:4537px;left:449px"><li>Rodent control</li><li>stored product pest control</li><li>Flying insect control</li><li>Ant</li><li>Spider &amp; insect control</li><li>Termite inspections &amp; treatments</li></ul>
<svg class="abs" style="top:4540px;left:804px" width="14" height="18" viewBox="0 0 14 18"><path d="M7 17S1 10 1 6.5a6 6 0 0112 0C13 10 7 17 7 17z" fill="none" stroke="#3d9313" stroke-width="1.6"/><circle cx="7" cy="6.5" r="2" fill="#3d9313"/></svg>
<p class="abs foot-contact" style="top:4536px;left:833px">BRIGHTMOOR PEST SERVICES<br>101 - Lorem ipsum simple text print</p>
<svg class="abs" style="top:4584px;left:803px" width="16" height="16" viewBox="0 0 16 16"><path d="M3 1l3 4-2 2q2 4 5 5l2-2 4 3-2 3Q3 15 1 3z" fill="#3d9313"/></svg>
<p class="abs foot-contact" style="top:4584px;left:833px">+(1) 555 014 2288</p>
<svg class="abs" style="top:4632px;left:803px" width="16" height="12" viewBox="0 0 16 12"><rect width="16" height="12" rx="1.5" fill="#3d9313"/><path d="M1 1.5l7 5 7-5" stroke="#050505" stroke-width="1.3" fill="none"/></svg>
<p class="abs foot-contact" style="top:4629px;left:833px">info@brightmoorpest.com</p>
<span class="abs brand-name" style="top:4740px;left:500px;width:200px;text-align:center;font-size:20px;line-height:22px;color:var(--white)">Brightmoor<br>Pest Services</span>
<p class="abs center-text" style="top:4811px;font-size:10px;color:#bdbdbd"><span style="color:var(--green)">©BRIGHTMOOR PEST SERVICES</span> - 2021 All rights reserved.</p>
<div class="abs" style="top:4852px;left:0;width:1200px;height:10px;background:var(--green)"></div>

</body>
</html>
```